" Pessoal, vamos lá! Estivemos trabalhando bastante e definindo o formato da nossa empresa e agora chegou a hora de passarmos para o nosso web site. Vamos lá: O " ÍNDICE" deverá conter: Nossos Serviços, Sua Obra Protegida, Tudo Melhor para Você, Peça um orçamento. 1- Ao clicar na aba Nossos Serviços. Será direcionado para Reforma & Construção; e Assessoria. Nesse campo terá as seguintes informações: Reforma & Construção * Projeto Guia de Reforma Fornecemos a planta com alterações e novas medidas. * Orçamento Enviamos nossa proposta de orçamento totalmente grátis. * Acompanhamento de Engenheiro Civil e Arquiteto* Equipe de profissionais capacitados. * Cotação de melhores preços de materiais; Auxiliamos na busca de melhores preços e condições de pagamento para a sua casa renova ou obra. * Seleção de parceiros para execução; Selecionamos profissionais capacitados para a execução da sua casa renova ou obra. Assessoria * Acompanhamos o projeto em execução Acompanhamento das atividades associadas ao planejamento, organização, direção e controle necessários para garantir o sucesso da sua casa renova ou obra. * Programação da Obra Compreendendo o detalhamento dos serviços e as providências preliminares, a programação dos materiais, mão de obra e equipamentos. * Relatórios de Andamento da obra Adequação do projeto e da construção às necessidades do cliente no que se refere à qualidade, prazo e custo. 2- Na aba " Sua Obra Protegida" ao clicar será direcionado para o campo com as seguintes informações: * Substituição de materiais danificados Qualquer material danificado por nossos profissionais ou fornecedores são repostos na mesma qualidade e quantidade, sem custos para o cliente. * Correção dos serviços mal executados* Mesmo buscando fornecer o resultado que você espera e sempre trabalhando com profissionais capacitados, erros podem acontecer. Diante disso, asseguramos a conclusão da sua obra com qualidade. * Troca de fornecedor Selecionamos os melhores profissionais do mercado. Mesmo assim, se você não gostar, é livre para nos solicitar a troca. 3- Já na aba " Tudo melhor para você" teremos as seguintes informações: * Orçamento gratuito * Gestão de pagamento * Prazo e rapidez * Saiba tudo que está acontecendo na sua casa renova * Garantia de Satisfação * Consultoria Técnica * Cronograma de gerenciamento * Otimização de custos * Equipe preparada 4- Seja um Novo Parceiro Ao clicar nessa frase aparecerá em uma nova janela duas opçoes: EMPRESA e PROFISSIONAL. Clicando em EMPRESA ficará a disposição para preenchimento os seguintes campos: Nome da Empresa, Nome do Responsável, Cidade, email, contato, área de especialidade ( nesse campo existirá opções para preenchimento) e campo para apresentação da empresa. Se clicar em PROFISSIONAL terá a disposição os seguintes itens: Nome, Telefone, cidade, email e área de especialidade (também várias opções )e um campo para digitação chamado de ESCREVA AQUI SUA MENSAGEM. 5- ORÇAMENTO Após o clique no ORÇAMENTO, o cliente terá à disposição 3 opções para um novo clique: REFORMA, CONSTRUÇÃO, ASSESSORIA (se possível, adicionar imagens aos nomes) • Após o clique em REFORMA abrirá um formulário com opções: Campo com opções de escolha de Casa, Apartamento ou loja comercial; Escolha do Cômodo (terá opções nesse campo) e nova janela referente a esta escolha para a digitação do tipo de serviço a ser executado nesse campo. Caso existam mais cômodos, existirá a opção de adicionar; opção de upload de arquivo; e campo para escrever alguma mensagem ou observação. • Clicando em CONSTRUÇÃO – O que pretende construir?; descreva detalhadamente o que pretende construir; opção de upload de arquivo; e campo para escrever alguma mensagem ou observação. • ASSESSORIA – Ajudamos você na gestão da sua casa renova. Como podemos ajudar? (aparecerá as opções de Cotação de preços; Busca de profissionais; Conferência e acompanhamento de serviços executados); descreva detalhadamente que tipo de ajuda você precisa em sua obra. 5.1 Ao final de todas as opções aparecerá campo para preenchimento dos dados do cliente: Seu nome; email; CEP; Rua; Numero/complemento; Bairro; Cidade; Estado; Telefone; e campo para clique em Aceito e concordo com os Termos de Uso e a Política de Privacidade. Confirmar envio da solicitação Para auxiliá-los vejam o site http://www.lajetorvix.com.br/orcamento.html 6- Vale lembrar que em cada aba terá que ser visualizado a opção de PEÇA UM ORÇAMENTO, FAÇA SUA CASA RENOVA, SUA CASA RENOVA AGORA.... FIQUEM A VONTADE com os dizeres. - Ao Final, na parte de contatos, endereço, rede social.... etc. Gostaríamos de deixar o espaço SEJA UM PARCEIRO. Queremos que ao clicar nessa item a empresa preencha um questionário. 7- Vale lembrar que ao clicar no item Peça orçamento o cliente será direcionado para um campo de preenchimento de dados. OBS IMPORTANTE: - Façam o uso de imagens modernas e suaves.. Queremos ser diferentes e inovadores e precisamos muito da criatividade de vocês. - Segue anexo um modelo de imagem que gostamos Segue anexo do escopo do nosso portfólio que será a cópia do nosso site. Aproveitem. "

```html
<!DOCTYPE html>
<html lang="pt-BR">
<head>
<meta charset="UTF-8">
<title>Casa Renova – Orçamento</title>
<link rel="stylesheet" href="https://fonts.googleapis.com/css2?family=Roboto:wght@300;400;500;700&display=swap">
<style>
  :root {
    --page: #ffffff;
    --navy-deep: #0f2a4f;
    --navy: #1b3f6e;
    --card: #163460;
    --card-active: #3a85cc;
    --footer: #2a5d97;
    --button: #2f6aa8;
    --text: #ffffff;
    --text-soft: #b9cbe3;
    --icon-tone: #e8eef7;
    --icon-disc: #16345f;
  }
  * { box-sizing: border-box; margin: 0; padding: 0; }
  html, body { width: 1200px; height: 1200px; overflow: hidden; }
  body {
    background: var(--page);
    font-family: "Roboto", Arial, sans-serif;
    color: var(--text);
    position: relative;
  }
  .site { position: absolute; left: 0; top: 233px; width: 1200px; }

  .topbar {
    height: 48px; background: var(--navy-deep);
    display: flex; align-items: center; justify-content: space-between;
    padding: 0 36px;
  }
  .brand { display: flex; align-items: center; gap: 8px; }
  .brand-mark { width: 22px; height: 22px; background: var(--text); flex: none; }
  .brand-text { display: flex; flex-direction: column; line-height: 1; }
  .brand-name { font-size: 19px; font-weight: 400; }
  .brand-tag { font-size: 5px; font-weight: 400; letter-spacing: .3px; margin-top: 2px; }

  .nav { display: flex; align-items: center; gap: 20px; }
  .nav-link { font-size: 8px; font-weight: 500; text-transform: uppercase; color: var(--text); text-decoration: none; white-space: nowrap; }
  .social-dot { width: 10px; height: 10px; border-radius: 50%; background: var(--text); }
  .nav-button {
    background: var(--button); color: var(--text);
    font-size: 8px; font-weight: 700; text-transform: uppercase;
    padding: 7px 18px; border-radius: 2px; margin-left: 6px; white-space: nowrap;
  }

  .quote {
    height: 595px; background: var(--navy);
    display: flex; flex-direction: column; align-items: center;
  }
  .quote-icon {
    width: 80px; height: 80px; border-radius: 50%;
    background: var(--icon-disc); margin-top: 52px;
  }
  .quote-title {
    margin-top: 30px; font-size: 29px; font-weight: 400; line-height: 34px;
    letter-spacing: 3px; text-transform: uppercase;
  }
  .quote-title strong { font-weight: 700; }
  .quote-sub { margin-top: 4px; font-size: 14px; font-weight: 300; color: var(--text-soft); letter-spacing: .5px; }

  .categories { display: flex; gap: 60px; margin-top: 28px; }
  .category {
    position: relative;
    width: 206px; height: 266px; background: var(--card);
    display: flex; flex-direction: column; align-items: center;
  }
  .category.is-active { background: var(--card-active); }
  .category-art {
    width: 140px; height: 90px; margin-top: 64px;
    background: linear-gradient(180deg, var(--icon-tone), #c9d6e8);
    border-radius: 6px; opacity: .9;
  }
  .category.is-active .category-art { background: linear-gradient(180deg, #2a6db0, #245f9c); }
  .category-label { margin-top: 22px; font-size: 20px; font-weight: 300; letter-spacing: 1px; }
  .category.is-active .category-label { color: #2664a1; }
  .pointer {
    position: absolute; left: 112px; top: 240px;
    width: 26px; height: 34px; background: var(--text); border-radius: 6px;
  }

  .footer {
    height: 84px; background: var(--footer);
    display: flex; align-items: center; justify-content: space-between;
    padding: 0 36px;
  }
  .footer .brand-mark { width: 46px; height: 46px; }
  .footer .brand-name { font-size: 26px; }
  .footer .brand-tag { font-size: 6px; }
  .footer .nav-button { background: var(--text); color: var(--navy-deep); }
</style>
</head>
<body>
  <div class="site">
    <header class="topbar">
      <div class="brand">
        <span class="brand-mark"></span>
        <span class="brand-text">
          <span class="brand-name">casa renova</span>
          <span class="brand-tag">REFORMA, CONSTRUÇÃO E ASSESSORIA</span>
        </span>
      </div>
      <nav class="nav">
        <a class="nav-link" href="#">Nossos Serviços</a>
        <a class="nav-link" href="#">Sua Obra Protegida</a>
        <a class="nav-link" href="#">Tudo Melhor Para Você</a>
        <span class="social-dot" role="img" aria-label="Rede social"></span>
        <span class="nav-button">Orçamento</span>
      </nav>
    </header>

    <main class="quote">
      <div class="quote-icon" role="img" aria-label="Ícone de documento de orçamento"></div>
      <h1 class="quote-title">Orçamento <strong>Rápido e Fácil</strong></h1>
      <p class="quote-sub">Por favor, indique abaixo qual a categoria do seu orçamento</p>

      <div class="categories">
        <div class="category">
          <div class="category-art" role="img" aria-label="Ícone de casa com ferramentas"></div>
          <span class="category-label">Reforma</span>
        </div>
        <div class="category">
          <div class="category-art" role="img" aria-label="Ícone de trabalhador com pá"></div>
          <span class="category-label">Construção</span>
        </div>
        <div class="category is-active">
          <div class="category-art" role="img" aria-label="Ícone de grupo de consultores"></div>
          <span class="category-label">Assessoria</span>
          <span class="pointer" role="img" aria-label="Cursor de mão"></span>
        </div>
      </div>
    </main>

    <footer class="footer">
      <div class="brand">
        <span class="brand-mark"></span>
        <span class="brand-text">
          <span class="brand-name">casa renova</span>
          <span class="brand-tag">REFORMA, CONSTRUÇÃO E ASSESSORIA</span>
        </span>
      </div>
      <nav class="nav">
        <a class="nav-link" href="#">Nossos Serviços</a>
        <a class="nav-link" href="#">Sua Obra Protegida</a>
        <a class="nav-link" href="#">Tudo Melhor Para Você</a>
        <span class="social-dot" role="img" aria-label="Rede social"></span>
        <span class="nav-button">Orçamento</span>
      </nav>
    </footer>
  </div>
</body>
</html>
```